Marigold Shore Realty business card design

Looking for an upscale and clean business card design and updated logo. I sell to a very high-end south Florida real estate market.
Target Market(s)
High-end real estate in south Florida real estate market
Industry/Entity Type
Real Estate Agent
Contact Information for Business Card
Marigold Shore Realty, Inc
738 West Penrick Ave, Suite 400/500, Fort Lauderdale, FL 33315
Tim Harlow - Broker/Owner
954-327-8846 Direct
timshomes@quillmail.net
Website: StayPenrickAv.net
Font styles to use
Other font styles liked:
- Copperplate Gothic, Georgia, etc.
Requirements
Must have
- My photo, company name, my name and title, all info stated in Details above
Nice to have
- Luxury home design element, waterfront

```html
<!DOCTYPE html>
<html lang="en">
<head>
<meta charset="utf-8">
<title>Marigold Shore Realty – Business Card</title>
<link rel="stylesheet" href="https://fonts.googleapis.com/css2?family=Alegreya:wght@700&family=Sorts+Mill+Goudy&family=Arimo:wght@400&display=swap">
<style>
  :root {
    --backdrop: #a3a3a3;
    --gold: #e2b520;
    --gold-light: #f5c935;
    --ink: #1f1f1f;
    --paper: #ffffff;
    --text: #1a1a1a;
    --rule: #9a9a9a;
    --photo-wall: #dcd8d0;
    --photo-jacket: #2a4a9a;
  }
  * { margin: 0; padding: 0; box-sizing: border-box; }
  html, body { width: 1200px; height: 1200px; overflow: hidden; }
  body { background: var(--backdrop); position: relative; }

  .card { position: absolute; top: 303px; height: 594px; overflow: hidden; }

  .card-front { left: 201px; width: 369px; }
  .front-pattern {
    position: absolute; inset: 0;
    background: radial-gradient(circle at 50% 50%, var(--gold-light) 0%, var(--gold) 75%);
  }
  .brand-disc {
    position: absolute; left: 20px; top: 133px; width: 328px; height: 328px;
    border-radius: 50%; background: var(--ink);
    display: flex; align-items: center; justify-content: center;
  }
  .brand-name {
    font-family: "Sorts Mill Goudy", Georgia, serif;
    color: var(--paper); font-size: 22px; line-height: 1.35;
    text-align: center; letter-spacing: 0.5px;
  }

  .card-back { left: 599px; width: 364px; background: var(--paper); }
  .agent-photo {
    position: absolute; left: 61px; top: 50px; width: 242px; height: 226px;
    border-radius: 10px;
    background: linear-gradient(180deg, var(--photo-wall) 0%, var(--photo-wall) 62%, var(--photo-jacket) 100%);
  }
  .agent-name {
    position: absolute; top: 298px; left: 0; right: 0; text-align: center;
    font-family: "Alegreya", Georgia, serif; font-weight: 700;
    font-size: 28px; color: var(--gold-light);
  }
  .agent-title {
    position: absolute; top: 332px; left: 0; right: 0; text-align: center;
    font-family: "Arimo", Arial, sans-serif; font-size: 16px; color: var(--text);
  }
  .icon-row {
    position: absolute; top: 364px; left: 88px; width: 190px; height: 25px;
    display: flex; align-items: center; gap: 4px;
  }
  .icon-row .rule { flex: 1; height: 1px; background: var(--rule); }
  .icon-row svg { width: 25px; height: 25px; }
  .contact-lines, .address-lines {
    position: absolute; left: 0; right: 0; text-align: center;
    font-family: "Arimo", Arial, sans-serif; font-size: 16px; line-height: 21.5px; color: var(--text);
  }
  .contact-lines { top: 399px; }
  .divider { position: absolute; top: 474px; left: 89px; width: 195px; height: 1px; background: var(--rule); }
  .address-lines { top: 490px; }
</style>
</head>
<body>
  <section class="card card-front">
    <div class="front-pattern" role="img" aria-label="Golden sunburst ray pattern"></div>
    <div class="brand-disc">
      <p class="brand-name">Marigold Shore<br>Realty, Inc.</p>
    </div>
  </section>

  <section class="card card-back">
    <div class="agent-photo" role="img" aria-label="Portrait photo of Tim Harlow"></div>
    <h1 class="agent-name">Tim Harlow</h1>
    <p class="agent-title">Broker/Owner</p>
    <div class="icon-row">
      <span class="rule"></span>
      <svg viewBox="0 0 25 25" aria-label="Phone"><rect width="25" height="25" rx="4" fill="#f5c935"/><path d="M6 10c0-2 3-3 6.5-3S19 8 19 10v1.5h-3V10H9v1.5H6z M8 12h9l1.5 6h-12z" fill="#fff"/></svg>
      <svg viewBox="0 0 25 25" aria-label="Email"><rect width="25" height="25" rx="4" fill="#f5c935"/><rect x="5.5" y="8" width="14" height="10" fill="none" stroke="#fff" stroke-width="1.4"/><path d="M5.5 8l7 5.5 7-5.5M5.5 18l5-4.5M19.5 18l-5-4.5" fill="none" stroke="#fff" stroke-width="1.2"/></svg>
      <svg viewBox="0 0 25 25" aria-label="Website"><rect width="25" height="25" rx="4" fill="#f5c935"/><circle cx="12.5" cy="12.5" r="6.5" fill="#fff"/><path d="M10 8.5c2 1 1 3 3 3.5s1 3-1 4M15.5 9c-1 1 0 2 1 2" fill="none" stroke="#f5c935" stroke-width="1.3"/></svg>
      <span class="rule"></span>
    </div>
    <p class="contact-lines">954-327-8846 Direct<br>timshomes@quillmail.net<br>www.StayPenrickAv.net</p>
    <div class="divider"></div>
    <p class="address-lines">738 West Penrick Ave<br>Suite 400/500<br>Fort Lauderdale, FL 33315</p>
  </section>
</body>
</html>
```